Modern claims management company

We need a new company presentation brochure, composed of about 20 pages in A4 format.
Cover, page 1 who we are, page 2 company profile, page 3 territorial operation, page from 4 to 10 services offered and description of services (The title of the page are: Perizie e Liquidazione danni, riparazioni e sostituzioni, teleclaimer, accertamento danni da fenomeno elettrico, TPA, Auditing, drone pilot, Valutazione rischi), from 11 to 17 specializations (Sinistri gravi, R.C., Tecnologici, Energie rinnovabili, strutture, ambiente) page 18 e 19 integrated services (perdite occulte, ricerca guasti, indagini termografiche, crisis management), page 20 clients ( list companies and logos) page 21 contact.
The company is made up of various companies, which belong to the principal, each of which deals with specific activities.
To date we already have various logos of the main company (Vardano and Pescetti) as well as the logos of the other companies. I load them on the portal.
Found then the graphic solution that we like we will have to proceed to make a presentation in similar powerpoint and the website.

Target Market(s)

Insurance Company, Insurance Broker

Font styles to use
Other font styles liked:
• ARIAL

Colors
333333
5c5c5c
959595
0392cd

Requirements
Must have
• It must be clear, professional and modern.
Nice to have
• I indicate some competitor sites, so that you can better understand what we are doing. www.torvellsgroup.example, www.harbridgeoakes.example, www.betadomaretti.example, www.gruppotavesi.example, www.vantuzzi.example.

```html
<!DOCTYPE html>
<html lang="en">
<head>
<meta charset="utf-8">
<title>Vardano and Pescetti – Brochure Outside</title>
<link href="https://fonts.googleapis.com/css2?family=Montserrat:wght@400;700;800&family=Arimo:wght@400&display=swap" rel="stylesheet">
<style>
:root{
  --backdrop:#8a8a8a;
  --paper:#ffffff;
  --paper-tint:#f1f1f2;
  --ink:#333333;
  --ink-soft:#5c5c5c;
  --ink-light:#959595;
  --brand:#0392cd;
  --brand-deep:#1c5d9c;
  --navy:#0f2a4d;
}
*{margin:0;padding:0;box-sizing:border-box}
html,body{width:902px;height:1200px;overflow:hidden}
body{background:var(--backdrop);font-family:"Arimo",Arial,sans-serif;color:var(--ink);position:relative}
.spread{position:absolute;left:21px;top:299px;width:860px;height:602px;background:var(--paper);box-shadow:0 10px 24px rgba(0,0,0,.35);overflow:hidden}
.page{position:absolute;top:0;height:100%;width:430px}
.page--back{left:0;background:linear-gradient(180deg,#fafafa,#f0f0f1)}
.page--front{left:430px;background:linear-gradient(180deg,#fbfbfb,#f2f2f3)}
.side-strip{position:absolute;left:0;top:0;width:144px;height:402px;background:var(--paper-tint)}
.side-frame{position:absolute;left:144px;top:0;width:194px;height:468px;border-right:1px solid #d6d6d6;border-bottom:1px solid #d6d6d6}
.side-name{position:absolute;left:44px;top:398px;transform-origin:0 0;transform:rotate(-90deg);white-space:nowrap;font-family:"Montserrat",sans-serif;width:380px}
.side-name .name{display:block;font-size:31px;font-weight:400;color:#e0e0e0;letter-spacing:.5px;line-height:1.1}
.side-name .tag{display:block;font-size:11px;color:#e2e2e2;letter-spacing:1px;margin-top:2px}
.photo{position:absolute;top:0;height:402px}
.photo--mono{left:144px;width:286px;background:linear-gradient(180deg,#9c9c9c 0%,#5d5d5d 30%,#4a4a4a 55%,#2c2c2c 80%,#4a4a4a 100%)}
.photo--colour{left:0;width:430px;background:linear-gradient(180deg,#8fb6d6 0%,#6b8fb3 22%,#c89a8e 34%,#23344f 48%,#1a2b44 70%,#2b5d8a 86%,#1c3a5e 100%)}
.top-rule{position:absolute;top:29px;height:1px;background:rgba(255,255,255,.7)}
.top-rule--back{left:25px;width:405px}
.top-rule--front{left:0;width:384px}
.headline-band{position:absolute;left:27px;top:296px;width:247px;height:106px;background:rgba(15,42,77,.82)}
.headline-frame{position:absolute;left:27px;top:296px;width:378px;height:174px;border:1px solid #cfcfcf}
.headline{position:absolute;left:40px;top:309px;color:#fff;font-family:"Montserrat",sans-serif;line-height:1}
.headline .l1{display:block;font-size:20px;font-weight:400}
.headline .l2{display:block;font-size:44px;font-weight:800;letter-spacing:-.5px;margin-top:-2px}
.headline .l3{display:block;font-size:24px;font-weight:400;margin-top:-1px}
.intro{position:absolute;left:48px;top:414px;width:336px;font-size:7.3px;line-height:1.35;text-align:center;color:var(--ink-soft)}
.brand{position:absolute;left:0;width:430px;top:505px;text-align:center;font-family:"Montserrat",sans-serif}
.brand .name{display:inline-flex;align-items:center;gap:8px;font-size:27px;font-weight:400;color:var(--brand-deep)}
.brand .mark{width:16px;height:16px;background:var(--brand)}
.brand .tag{display:block;font-size:10px;color:var(--ink-light);letter-spacing:1px;margin-top:1px}
.site{position:absolute;left:0;width:430px;top:558px;text-align:center;font-family:"Montserrat",sans-serif;font-size:7px;letter-spacing:3.6px;color:var(--ink)}
.about{position:absolute;left:34px;top:436px;width:171px;font-size:7px;line-height:1.45;text-align:justify;color:var(--ink-soft)}
.contact{position:absolute;left:242px;top:524px;font-size:7.3px;font-style:normal;color:var(--ink-soft)}
.contact h2{font-family:"Montserrat",sans-serif;font-size:7.3px;font-weight:400;color:var(--ink);margin-bottom:3px}
.contact ul{list-style:none}
.contact li{display:flex;align-items:center;gap:6px;height:10px}
.contact svg{width:7px;height:7px;flex:none}
</style>
</head>
<body>
<main class="spread">
  <section class="page page--back">
    <div class="side-strip"></div>
    <div class="photo photo--mono" role="img" aria-label="Black and white photograph of a waterfront city at dusk"></div>
    <div class="side-frame"></div>
    <div class="top-rule top-rule--back"></div>
    <div class="side-name"><span class="name">Vardano and Pescetti</span><span class="tag">consulenza peritale per le assicurazioni</span></div>
    <p class="about">Lorem Ipsum is simply dummy text of the printing and typesetting industry. Lorem Ipsum has been the industry's standard dummy text ever since the 1500s, Lorem Ipsum is simply dummy text of the printing and typesetting industry. Lorem Ipsum has been the industry's standard dummy text ever since the 1500s,Lorem Ipsum is simply dummy text of the printing and typesetting industry. Lorem Ipsum has been the industry's standard dummy text ever since the 1500s. Lorem Ipsum is simply dummy text of the printing and typesetting industry. Lorem Ipsum has been the industry's standard dummy text ever since the 1500s.</p>
    <address class="contact">
      <h2>CONTACT US:</h2>
      <ul>
        <li><svg viewBox="0 0 10 10"><circle cx="5" cy="5" r="5" fill="#0392cd"/><path d="M5 2.2a1.8 1.8 0 0 0-1.8 1.8C3.2 5.4 5 7.8 5 7.8S6.8 5.4 6.8 4A1.8 1.8 0 0 0 5 2.2z" fill="#fff"/></svg>Via Lorenzi 14, Milano</li>
        <li><svg viewBox="0 0 10 10"><circle cx="5" cy="5" r="5" fill="#0392cd"/><path d="M3 2.5l1.2 1.2-.6.9c.4.8 1 1.4 1.8 1.8l.9-.6L7.5 7 6.8 7.7C4.8 7.5 2.5 5.2 2.3 3.2z" fill="#fff"/></svg>+39 02 555 0147, +39 02 555 0148</li>
        <li><svg viewBox="0 0 10 10"><circle cx="5" cy="5" r="5" fill="#0392cd"/><rect x="2.6" y="3.3" width="4.8" height="3.4" fill="none" stroke="#fff" stroke-width=".7"/><path d="M2.6 3.3L5 5.2l2.4-1.9" fill="none" stroke="#fff" stroke-width=".7"/></svg>info@vardanopescetti.example</li>
        <li><svg viewBox="0 0 10 10"><circle cx="5" cy="5" r="5" fill="#0392cd"/><circle cx="5" cy="5" r="2.6" fill="none" stroke="#fff" stroke-width=".7"/><path d="M2.4 5h5.2M5 2.4v5.2" stroke="#fff" stroke-width=".6"/></svg>www.vardanopescetti.example</li>
      </ul>
    </address>
  </section>
  <section class="page page--front">
    <div class="photo photo--colour" role="img" aria-label="Colour photograph of a city skyline over the river at twilight"></div>
    <div class="top-rule top-rule--front"></div>
    <div class="headline-band"></div>
    <div class="headline-frame"></div>
    <h1 class="headline"><span class="l1">LOREM IPSUM</span><span class="l2">IS SIMPLY</span><span class="l3">DUMMY TEXT</span></h1>
    <p class="intro">Lorem Ipsum is simply dummy text of the printing and typesetting industry. Lorem Ipsum has been the industry's standard dummy text ever since the 1500s. Lorem Ipsum is simply dummy text of the printing and typesetting industry. Lorem Ipsum has been the industry's standard dummy text ever since the 1500s.</p>
    <div class="brand"><span class="name"><span class="mark"></span>Vardano and Pescetti</span><span class="tag">consulenza peritale per le assicurazioni</span></div>
    <p class="site">WWW.VARDANOPESCETTI.EXAMPLE</p>
  </section>
</main>
</body>
</html>
```